Marbella Specialty Coffee needs a Packaging design

We need packaging design for coffee that suits our brand identity, that is the best quality in Mexico.
We only sell mexican coffee with Q scores above 80
We are evaluating 3 types of packaging: Bag, Box and Cillinder can
The specific package format will be decided based on the designs that we get.

Target Market(s)

Coffee experts and enthusiast.
People that relate the Coffee consumption and experience with wine tasting and Bon Vivant way

Requirements
Should not have
• Photos any mexican cliché

```html
<!DOCTYPE html>
<html lang="en">
<head>
<meta charset="utf-8">
<title>Marbella Specialty Coffee – Mexican Roast Ground Coffee Package</title>
<link rel="stylesheet" href="https://fonts.googleapis.com/css2?family=Cabin:ital,wght@0,500;0,700;1,500&family=Montserrat:wght@700&display=swap">
<style>
  :root {
    --green: #0b9a4c;
    --black: #000000;
    --pink: #e8267f;
    --red: #ea2129;
    --orange: #f9ad43;
    --gold: #f6b246;
    --brand-gold: #c9952f;
    --ink: #111111;
  }
  html, body {
    margin: 0;
    padding: 0;
    overflow: hidden;
    background: #ffffff;
  }
  .package {
    position: relative;
    width: 688px;
    height: 1200px;
    overflow: hidden;
  }
  .band {
    position: absolute;
    left: 0;
    width: 100%;
  }
  .band--grind { top: 0; height: 234px; background: var(--green); }
  .band--brand { top: 234px; height: 256px; background: var(--black); }
  .band--pink { top: 490px; height: 237px; background: var(--pink); }
  .band--red { top: 727px; height: 241px; background: var(--red); }
  .band--orange { top: 968px; height: 232px; background: var(--orange); }

  .grind-type {
    margin: 0;
    position: absolute;
    top: 108px;
    width: 100%;
    text-align: center;
    font-family: "Montserrat", sans-serif;
    font-weight: 700;
    font-size: 42px;
    letter-spacing: 0.5px;
    color: var(--ink);
  }

  .brand {
    position: absolute;
    top: 0;
    left: 0;
    width: 100%;
    height: 100%;
    display: flex;
    align-items: center;
    justify-content: center;
    gap: 22px;
  }
  .brand-dot {
    width: 34px;
    height: 34px;
    border-radius: 50%;
    background: var(--brand-gold);
  }
  .brand-name {
    font-family: "Cabin", sans-serif;
    font-weight: 500;
    font-size: 42px;
    color: var(--brand-gold);
  }

  .flavour-badge {
    position: absolute;
    left: 102px;
    top: 614px;
    width: 486px;
    height: 486px;
  }
  .flavour-text {
    position: absolute;
    left: 102px;
    top: 614px;
    width: 486px;
    height: 486px;
    text-align: center;
    font-family: "Cabin", sans-serif;
    color: var(--gold);
  }
  .roast-name {
    margin: 0;
    position: absolute;
    top: 118px;
    width: 100%;
    font-weight: 500;
    font-size: 42px;
  }
  .roast-icon {
    position: absolute;
    left: 225px;
    top: 214px;
    width: 36px;
    height: 36px;
    border-radius: 50%;
    background: var(--gold);
  }
  .roast-notes {
    margin: 0;
    position: absolute;
    top: 302px;
    width: 100%;
    font-style: italic;
    font-weight: 500;
    font-size: 35px;
  }

  .net-weight {
    margin: 0;
    position: absolute;
    top: 1128px;
    width: 100%;
    text-align: center;
    font-family: Arial, "Helvetica Neue", sans-serif;
    font-size: 24px;
    color: var(--ink);
  }
</style>
</head>
<body>
  <main class="package">
    <section class="band band--grind">
      <h2 class="grind-type">GROUND</h2>
    </section>

    <section class="band band--brand">
      <div class="brand">
        <span class="brand-dot"></span>
        <span class="brand-name">Marbella Specialty Coffee</span>
      </div>
    </section>

    <div class="band band--pink"></div>
    <div class="band band--red"></div>
    <div class="band band--orange"></div>

    <svg class="flavour-badge" viewBox="0 0 486 486" aria-hidden="true">
      <circle cx="243" cy="243" r="232" fill="var(--green)"/>
      <circle cx="243" cy="243" r="214" fill="var(--black)"/>
    </svg>

    <div class="flavour-text">
      <h1 class="roast-name">Mexican Roast</h1>
      <span class="roast-icon" role="img" aria-label="Small heart pierced by an arrow icon"></span>
      <p class="roast-notes">Bold and smoky</p>
    </div>

    <p class="net-weight">NET WT 12 oz (340g)</p>
  </main>
</body>
</html>
```